Business card design for Virtual Assistance company

I need a business card designed for my virtual assistance company. We are a small company who services primarily C-level executive clients. The card needs to be double sided with the following contact information on the back:
Melissa Hartwell
Owner/CEO
info@pkrsolutions.net
www.pkrsolutions.net
310.552.9083

The front side should just have the company name incorporated: "PKR Solutions" and "virtual assistance"

The card should be simplistic, but eye catching and should speak to high level executives. Our primary focus areas consist of executive assistance and government contracting.

Target Market(s)

CEOs and executives

Contact Information for Business Card

see project description. phone, email, website.

Colors

Designer to choose only greyscale colors for use in the design.

```html
<!DOCTYPE html>
<html lang="en">
<head>
<meta charset="utf-8">
<title>PKR Solutions — Business Card</title>
<link rel="stylesheet" href="https://fonts.googleapis.com/css2?family=Bodoni+Moda:wght@700&family=Lato:wght@400&display=swap">
<style>
  :root {
    --backdrop: #bdbdbd;
    --card-dark: #3a3938;
    --card-light: #ffffff;
    --ink-light: #ffffff;
    --ink-dark: #333333;
    --rule-dark: #6d6d6d;
  }
  * { margin: 0; padding: 0; box-sizing: border-box; }
  html, body {
    width: 1200px; height: 1000px; overflow: hidden;
    background: var(--backdrop);
  }
  .canvas { position: relative; width: 1200px; height: 1000px; }
  .card {
    position: absolute; left: 187px; width: 826px; height: 471px;
    border-radius: 18px;
  }
  .card--front { top: 21px; background: var(--card-dark); color: var(--ink-light); }
  .card--back { top: 507px; background: var(--card-light); color: var(--ink-dark); }

  .company-name {
    position: absolute; left: 0; right: 0; top: 180px;
    text-align: center;
    font-family: "Lato", Arial, sans-serif;
    font-weight: 400; font-size: 54px; line-height: 64px;
    letter-spacing: 1px;
  }
  .company-service {
    position: absolute; left: 0; right: 0; top: 258px;
    text-align: center;
    font-family: "Lato", Arial, sans-serif;
    font-weight: 400; font-size: 22px; line-height: 30px;
    letter-spacing: 1px;
  }

  .contact-block { position: absolute; left: 208px; top: 122px; }
  .person-name {
    font-family: "Bodoni Moda", "Didot", serif;
    font-weight: 700; font-size: 33px; line-height: 44px;
    letter-spacing: 1px;
  }
  .person-title {
    font-family: "Lato", Arial, sans-serif;
    font-size: 22.5px; line-height: 30px; margin-top: 1px;
  }
  .contact-rule {
    width: 154px; height: 1px; background: var(--rule-dark);
    margin: 29px 0 32px 1px;
  }
  .contact-list { list-style: none; }
  .contact-item {
    display: flex; align-items: center; height: 34.5px;
    font-family: "Lato", Arial, sans-serif; font-size: 22.5px;
  }
  .contact-icon { width: 16px; height: 16px; margin: 4px 17px 0 0; fill: var(--ink-dark); }
</style>
</head>
<body>
<main class="canvas">
  <section class="card card--front">
    <h1 class="company-name">PKR Solutions</h1>
    <p class="company-service">Virtual Assistance</p>
  </section>

  <section class="card card--back">
    <div class="contact-block">
      <h2 class="person-name">MELISSA HARTWELL</h2>
      <p class="person-title">OWNER / CEO</p>
      <div class="contact-rule"></div>
      <ul class="contact-list">
        <li class="contact-item">
          <svg class="contact-icon" viewBox="0 0 16 16" aria-hidden="true">
            <path d="M3.5 1.5l2.2 2.8-1.2 1.6c.9 2 2.5 3.6 4.5 4.5l1.6-1.2 2.8 2.2-1.4 2.2C6.5 13.5 2.5 9.5 1.4 3z"/>
            <path d="M9 2a5 5 0 0 1 5 5h-1.3A3.7 3.7 0 0 0 9 3.3zM9 4.6A2.4 2.4 0 0 1 11.4 7h-1.2A1.2 1.2 0 0 0 9 5.8z"/>
          </svg>
          <span>310.552.9083</span>
        </li>
        <li class="contact-item">
          <svg class="contact-icon" viewBox="0 0 16 16" aria-hidden="true">
            <path d="M15 1.5L1 7.5l4.5 1.6L13 3.5 7 10v4.5l2.5-3.2 3 1.7z"/>
          </svg>
          <span>info@pkrsolutions.net</span>
        </li>
        <li class="contact-item">
          <svg class="contact-icon" viewBox="0 0 16 16" aria-hidden="true">
            <path fill-rule="evenodd" d="M8 1a7 7 0 1 0 0 14A7 7 0 0 0 8 1zm0 1.4c.8.9 1.4 2.2 1.6 3.6H6.4C6.6 4.6 7.2 3.3 8 2.4zM2.5 9.3a5.6 5.6 0 0 1 0-2.6h2.6a10 10 0 0 0 0 2.6zm.6 1.4h2.2c.2 1 .6 2 1.1 2.8a5.6 5.6 0 0 1-3.3-2.8zm3.3 0h3.2c-.2 1.3-.8 2.4-1.6 3.3-.8-.9-1.400-2-1.6-3.3zm4.3 0h2.2a5.6 5.6 0 0 1-3.3 2.8c.5-.8.9-1.8 1.1-2.8zm2.8-1.4h-2.6a10 10 0 0 0 0-2.6h2.6a5.6 5.6 0 0 1 0 2.6zM9.3 9.3H6.7a8.8 8.8 0 0 1 0-2.6h2.6a8.8 8.8 0 0 1 0 2.6z"/>
          </svg>
          <span>www.pkrsolutions.net</span>
        </li>
      </ul>
    </div>
  </section>
</main>
</body>
</html>
```